Ridgeline Outfitters Business Cards

Recently had a logo done with Artflockr and now looking for a business card to go along with it.

Target Market(s)

Ridgeline Outfitters is a weapons dealer. My market will be primarily men, hunting, shooting type.

Industry/Entity Type

Business

Contact Information for Business Card

I selected double sided, but this is not required, single or double is going to be fine. I picture the logo on one side, or perhaps just the circle which contains "RO" with the remaining info on the other side.

Font styles to use
Sans Serif

Requirements
Must have
• My name: Wesley Holm
• Title: Owner
• tel: 612-555-0378
• web: www.ridgelineoutfittersmn.example
Nice to have
• I like the concept of a black business card. I would like to keep the colors monotone, black, grey, white or red. Red is acceptable because it is in the logo. I have also seen cards that are matte black with shiny black as well, perhaps for the logo (or circle RO) part of the logo.
• I will upload a couple of the logos for use, and also an example I just found of the black on black. and some others that have a nice contrast.
Should not have
• lots of colors are not wanted.

```html
<!DOCTYPE html>
<html lang="en">
<head>
<meta charset="utf-8">
<title>Ridgeline Outfitters Business Cards</title>
<link rel="stylesheet" href="https://fonts.googleapis.com/css2?family=Oswald:wght@300;400;600&display=swap">
<style>
  :root {
    --bg-centre: #4a4a4a;
    --bg-edge: #2f2f2f;
    --card-dark: #161616;
    --card-mid: #242424;
    --band: #050505;
    --brand-red: #d0262c;
    --steel-grey: #8a8a8a;
    --text-grey: #9c9c9c;
  }
  * { box-sizing: border-box; margin: 0; padding: 0; }
  html, body { width: 1200px; height: 1200px; overflow: hidden; }
  body {
    background: radial-gradient(circle at 50% 50%, var(--bg-centre), var(--bg-edge) 70%);
    font-family: "Oswald", sans-serif;
    position: relative;
  }
  .card {
    position: absolute;
    left: 250px;
    width: 700px;
    height: 400px;
    background: linear-gradient(135deg, var(--card-mid) 0%, var(--card-dark) 45%, var(--card-mid) 70%, var(--card-dark) 100%);
    box-shadow: 0 14px 30px rgba(0,0,0,0.45);
    overflow: hidden;
  }
  .card--front { top: 150px; }
  .card--back { top: 650px; }

  .brand-name {
    position: absolute;
    top: 108px;
    left: 0; right: 0;
    text-align: center;
    color: var(--brand-red);
    font-weight: 600;
    font-size: 44px;
    letter-spacing: 4px;
    text-transform: uppercase;
  }
  .holder {
    position: absolute;
    top: 196px;
    left: 0; right: 0;
    text-align: center;
    color: var(--steel-grey);
    text-transform: uppercase;
  }
  .holder__name { font-weight: 400; font-size: 24px; letter-spacing: 3px; line-height: 1.1; }
  .holder__title { font-weight: 300; font-size: 13px; letter-spacing: 2px; }

  .contact-band {
    position: absolute;
    left: 0; right: 0;
    top: 300px;
    height: 44px;
    background: var(--band);
    display: flex;
    align-items: center;
    gap: 46px;
    padding-left: 60px;
    color: var(--text-grey);
    font-weight: 400;
    font-size: 19px;
    letter-spacing: 2px;
    text-transform: uppercase;
    white-space: nowrap;
  }
  .contact-item { display: flex; align-items: center; gap: 12px; }
  .contact-item svg { width: 18px; height: 18px; fill: var(--text-grey); flex: none; }

  .back-brand {
    position: absolute;
    left: 0; right: 0; top: 0; bottom: 0;
    display: flex;
    align-items: center;
    justify-content: center;
    gap: 18px;
  }
  .back-brand__dot {
    width: 22px; height: 22px;
    border-radius: 50%;
    background: var(--steel-grey);
    flex: none;
  }
  .back-brand__name {
    color: var(--brand-red);
    font-weight: 600;
    font-size: 36px;
    letter-spacing: 3px;
    text-transform: uppercase;
    white-space: nowrap;
  }
</style>
</head>
<body>
  <section class="card card--front" aria-label="Business card front">
    <h1 class="brand-name">Ridgeline Outfitters</h1>
    <div class="holder">
      <p class="holder__name">Wesley Holm</p>
      <p class="holder__title">Owner</p>
    </div>
    <div class="contact-band">
      <span class="contact-item">
        <svg viewBox="0 0 24 24" aria-hidden="true"><path d="M6.6 10.8a15.1 15.1 0 0 0 6.6 6.6l2.2-2.2a1 1 0 0 1 1-.25 11.4 11.4 0 0 0 3.6.57 1 1 0 0 1 1 1V20a1 1 0 0 1-1 1A17 17 0 0 1 3 4a1 1 0 0 1 1-1h3.5a1 1 0 0 1 1 1c0 1.25.2 2.45.57 3.57a1 1 0 0 1-.25 1z"/></svg>
        612-555-0378
      </span>
      <span class="contact-item">
        <svg viewBox="0 0 24 24" aria-hidden="true"><circle cx="12" cy="12" r="10"/><path d="M8 7c2 1 3 0 4 2s-1 3 1 4 1 4 3 4" stroke="#050505" stroke-width="2" fill="none"/></svg>
        www.ridgelineoutfittersmn.example
      </span>
    </div>
  </section>

  <section class="card card--back" aria-label="Business card back">
    <div class="back-brand">
      <span class="back-brand__dot" aria-hidden="true"></span>
      <span class="back-brand__name">Ridgeline Outfitters</span>
    </div>
  </section>
</body>
</html>
```